Brindle Offers is an online marketing platform.

A daily deals site for consumers a way to bring in new clients for clients and this is who the business cards are for. Industries - Food and Drink, Things To Do, Beauty and Spas, Staycations and Services.
Logo on one side.
Name - Owen Radley
Job Title - Sales Director
Phone Number - 07912358046
Email - owen@brindleoffers.co.uk
need same for second person
Name - Fiona Bracken
Job Title - Operations Director
Phone Number - 01632840275
Email - fiona@brindleoffers.co.uk
Bottom Right - Chatterbook Icon, Snapa Icon, Pipline Icon
Target Market(s)
Business owners of the above industries
Contact Information for Business Card
Name - Owen Radley
Name - Fiona Bracken
Look and feel

```html
<!DOCTYPE html>
<html lang="en">
<head>
<meta charset="utf-8">
<title>Brindle Offers – Business Card</title>
<link rel="stylesheet" href="https://fonts.googleapis.com/css2?family=Jost:wght@400;500;600;700&display=swap">
<style>
  :root {
    --brand-blue: #074c93;
    --band-blue: #2a5fb3;
    --band-grey: #4a4a4a;
    --paper: #f0f0f0;
    --page: #e4e4e4;
    --white: #ffffff;
  }
  * { box-sizing: border-box; margin: 0; padding: 0; }
  html, body {
    width: 1200px; height: 1200px; overflow: hidden;
    background: var(--page);
    font-family: "Jost", sans-serif;
  }
  .card {
    position: absolute; left: 228px; width: 744px; height: 424px;
    border-radius: 40px; overflow: hidden; background: var(--brand-blue);
  }
  .card--front { top: 136px; }
  .card--back { top: 640px; }
  .card__bg { position: absolute; inset: 0; width: 100%; height: 100%; }

  .brand { position: absolute; display: flex; flex-direction: column; }
  .brand__row { display: flex; align-items: center; gap: 10px; }
  .brand__dot { border-radius: 50%; flex: none; }
  .brand__name { font-weight: 600; line-height: 1; white-space: nowrap; }
  .brand__tagline { letter-spacing: 0.12em; font-weight: 500; white-space: nowrap; }

  .card--front .brand { left: 28px; top: 168px; }
  .card--front .brand__dot { width: 44px; height: 44px; background: var(--brand-blue); }
  .card--front .brand__name { font-size: 33px; color: var(--brand-blue); }
  .card--front .brand__tagline { font-size: 17px; color: var(--band-grey); margin: 6px 0 0 54px; }

  .contact { position: absolute; right: 26px; top: 134px; text-align: right; color: var(--white); }
  .contact__name { font-size: 22px; font-weight: 600; letter-spacing: 0.01em; }
  .contact__role { font-size: 16px; font-weight: 400; margin-top: -2px; }
  .contact__list { list-style: none; margin-top: 40px; }
  .contact__item { display: flex; justify-content: flex-end; align-items: center; gap: 8px; font-size: 16px; height: 24px; }
  .contact__icon { width: 18px; height: 18px; flex: none; }

  .card--back .brand { left: 50%; top: 150px; transform: translateX(-50%); align-items: flex-end; }
  .card--back .brand__dot { width: 72px; height: 72px; background: var(--white); }
  .card--back .brand__name { font-size: 54px; color: var(--white); }
  .card--back .brand__tagline { font-size: 26px; color: var(--white); margin-top: 10px; }

  .social { position: absolute; left: 0; right: 0; top: 360px; display: flex; justify-content: center; gap: 18px; }
  .social__item { display: flex; align-items: center; gap: 6px; color: var(--white); font-size: 14px; font-weight: 500; }
  .social__dot { width: 14px; height: 14px; border-radius: 50%; background: var(--white); }
</style>
</head>
<body>

<section class="card card--front">
  <svg class="card__bg" viewBox="0 0 930 530" preserveAspectRatio="none" aria-hidden="true">
    <rect width="930" height="530" fill="var(--brand-blue)"/>
    <path d="M0,0 H535 C585,150 545,400 420,530 H0 Z" fill="var(--band-blue)"/>
    <path d="M0,0 H508 C558,150 518,395 395,530 H0 Z" fill="var(--band-grey)"/>
    <path d="M0,0 H455 C530,160 495,400 365,530 H0 Z" fill="var(--paper)"/>
  </svg>

  <div class="brand">
    <div class="brand__row">
      <span class="brand__dot"></span>
      <span class="brand__name">Brindle Offers</span>
    </div>
    <span class="brand__tagline">SAVE. SHOP. ENJOY.</span>
  </div>

  <div class="contact">
    <p class="contact__name">OWEN RADLEY</p>
    <p class="contact__role">Sales Director</p>
    <ul class="contact__list">
      <li class="contact__item">07912358046
        <svg class="contact__icon" viewBox="0 0 20 20" aria-hidden="true"><circle cx="10" cy="10" r="10" fill="#fff"/><path d="M6.5 5 L8.5 5 L9.3 7.6 L8.2 8.6 Q9.4 11 11.4 11.9 L12.4 10.8 L15 11.6 L15 13.6 Q12 15.5 8.5 12 Q5 8.5 6.5 5 Z" fill="var(--brand-blue)"/></svg>
      </li>
      <li class="contact__item">owen@brindleoffers.co.uk
        <svg class="contact__icon" viewBox="0 0 20 20" aria-hidden="true"><circle cx="10" cy="10" r="10" fill="#fff"/><rect x="5" y="6.5" width="10" height="7" fill="none" stroke="var(--brand-blue)" stroke-width="1.4"/><path d="M5 6.5 L10 10.5 L15 6.5" fill="none" stroke="var(--brand-blue)" stroke-width="1.4"/></svg>
      </li>
      <li class="contact__item">www.brindleoffers.co.uk
        <svg class="contact__icon" viewBox="0 0 20 20" aria-hidden="true"><circle cx="10" cy="10" r="10" fill="#fff"/><circle cx="10" cy="10" r="5.5" fill="none" stroke="var(--brand-blue)" stroke-width="1.3"/><ellipse cx="10" cy="10" rx="2.3" ry="5.5" fill="none" stroke="var(--brand-blue)" stroke-width="1.1"/><path d="M4.5 10 H15.5" stroke="var(--brand-blue)" stroke-width="1.1"/></svg>
      </li>
    </ul>
  </div>
</section>

<section class="card card--back">
  <div class="brand">
    <div class="brand__row">
      <span class="brand__dot"></span>
      <span class="brand__name">Brindle Offers</span>
    </div>
    <span class="brand__tagline">SAVE. SHOP. ENJOY.</span>
  </div>

  <div class="social">
    <span class="social__item"><span class="social__dot"></span>Chatterbook</span>
    <span class="social__item"><span class="social__dot"></span>Snapa</span>
    <span class="social__item"><span class="social__dot"></span>Pipline</span>
  </div>
</section>

</body>
</html>
```